Redesign of an insurance website

Attached is an insurance website that I need to redesign. Currently the website is too dark. I like for example www.brenvalo.com . Could you make the website lighter and change the structure a little so that it is more user friendly?

Industry/Entity Type

Insurance

Number of Pages Required

4 page

```html
<!DOCTYPE html>
<html lang="en">
<head>
<meta charset="utf-8">
<title>JistotaPlus.cz – Insurance</title>
<link href="https://fonts.googleapis.com/css2?family=Poppins:wght@400;500;600;700&display=swap" rel="stylesheet">
<style>
:root{
  --blue:#1f6fe5;
  --blue-dark:#0d2b6b;
  --orange:#ff6a1a;
  --ink:#2a2f3a;
  --muted:#8a93a3;
  --sky:#e9f3fc;
  --sky-2:#d5e8f8;
  --line:#e3e8ef;
  --white:#ffffff;
}
*{box-sizing:border-box;margin:0;padding:0}
html,body{width:776px;height:1200px;overflow:hidden}
body{font-family:"Poppins",sans-serif;color:var(--ink);background:var(--white);position:relative}
.abs{position:absolute}
a{color:inherit;text-decoration:none}

/* header */
.site-header{position:absolute;top:0;left:0;width:776px;height:40px;z-index:3}
.brand{position:absolute;left:30px;top:10px;font-weight:700;font-size:15px;color:var(--blue);letter-spacing:.3px}
.main-nav{position:absolute;left:350px;top:14px;display:flex;gap:26px;font-size:7px;line-height:10px;color:var(--ink);white-space:nowrap}
.btn-login,.btn-register{position:absolute;top:10px;height:17px;border-radius:9px;font-size:6.5px;font-weight:600;display:flex;align-items:center;justify-content:center;width:48px}
.btn-login{left:546px;border:1px solid var(--orange);color:var(--orange)}
.btn-register{left:606px;background:var(--blue);color:var(--white)}

/* hero */
.hero{position:absolute;top:0;left:0;width:776px;height:340px;background:var(--sky);overflow:hidden}
.hero-waves{position:absolute;left:0;top:180px}
.hero-title{position:absolute;left:44px;top:108px;font-size:22px;line-height:25px;font-weight:500;color:var(--ink)}
.hero-sub{position:absolute;left:44px;top:162px;width:140px;font-size:6.5px;line-height:10px;color:var(--muted)}
.btn-start{position:absolute;left:44px;top:202px;width:62px;height:20px;border-radius:10px;background:var(--blue);color:var(--white);font-size:6px;font-weight:600;display:flex;align-items:center;justify-content:center}
.hero-art{position:absolute;left:300px;top:60px;width:180px;height:210px;border-radius:90px 90px 20px 20px;background:radial-gradient(circle at 50% 45%,#f6c7a8 0,#f2a97e 22%,#8cc4f0 50%,rgba(233,243,252,0) 72%)}
.phone{position:absolute;left:500px;top:52px;width:180px;height:248px;border-radius:22px;background:var(--white);box-shadow:0 6px 18px rgba(30,80,150,.15);border:1px solid var(--line)}
.phone-badge{position:absolute;left:76px;top:34px;width:26px;height:26px;border-radius:50%;background:var(--blue)}
.phone-title{position:absolute;left:0;width:178px;top:64px;text-align:center;font-size:5px;color:var(--blue);font-weight:600}
.field{position:absolute;left:30px;width:118px;height:14px;border:1px solid var(--line);border-radius:7px;font-size:5px;color:var(--muted);padding-left:14px;display:flex;align-items:center}
.field::before{content:"";position:absolute;left:5px;width:5px;height:5px;border-radius:50%;background:var(--sky-2)}
.phone-submit{position:absolute;left:54px;top:162px;width:70px;height:14px;border-radius:7px;background:var(--orange)}

/* section headings */
.section-title{position:absolute;left:0;width:776px;text-align:center;font-size:15px;font-weight:600;color:var(--ink)}
.section-lead{position:absolute;left:228px;width:320px;text-align:center;font-size:5.5px;line-height:9px;color:var(--muted)}

/* services */
.service-card{position:absolute;top:458px;width:108px;height:106px;background:var(--white);border-radius:4px;box-shadow:0 4px 14px rgba(20,50,100,.10);text-align:center}
.service-icon{position:absolute;left:38px;top:18px;width:32px;height:26px;border-radius:6px}
.service-name{position:absolute;top:55px;left:0;width:108px;font-size:6px;font-weight:700;color:var(--ink)}
.service-text{position:absolute;top:66px;left:16px;width:76px;font-size:4.8px;line-height:7px;color:var(--muted)}
.slider-arrow{position:absolute;top:502px;width:16px;height:16px;border-radius:50%;background:var(--blue)}

/* about */
.about-art{position:absolute;left:138px;top:830px;width:180px;height:132px;border-radius:6px;background:linear-gradient(160deg,#f4f8fd,#dbe9f7);box-shadow:0 6px 16px rgba(20,50,100,.12)}
.about-heading{position:absolute;left:400px;top:858px;font-size:8px;font-weight:600;color:var(--ink)}
.about-text{position:absolute;left:400px;top:874px;width:150px;font-size:5px;line-height:8px;color:var(--muted)}
.btn-more{position:absolute;left:400px;top:920px;width:52px;height:14px;border-radius:7px;background:var(--blue);color:var(--white);font-size:4.8px;font-weight:600;display:flex;align-items:center;justify-content:center}

/* footer */
.site-footer{position:absolute;left:0;top:1010px;width:776px;height:190px;background:var(--sky)}
.footer-brand{position:absolute;left:28px;top:16px;font-size:13px;font-weight:700;color:var(--blue)}
.footer-about{position:absolute;left:28px;top:44px;width:150px;font-size:5px;line-height:8px;color:var(--muted)}
.social{position:absolute;top:70px;width:11px;height:11px;border-radius:50%}
.footer-col{position:absolute;top:18px;font-size:5px;line-height:10px;color:var(--muted);white-space:nowrap}
.footer-col h4{font-size:6.5px;font-weight:600;color:var(--ink);margin-bottom:4px}
.contact-row{display:flex;gap:6px;align-items:center}
.subscribe{position:absolute;left:500px;top:88px;width:168px;height:14px;background:var(--white);border-radius:2px;font-size:5px;color:var(--muted);padding-left:6px;display:flex;align-items:center}
.subscribe-btn{position:absolute;right:0;top:0;width:40px;height:14px;background:var(--blue);border-radius:2px}
.copyright{position:absolute;left:0;top:172px;width:776px;text-align:center;font-size:4.8px;color:var(--muted)}
</style>
</head>
<body>

<section class="hero">
  <svg class="hero-waves" width="776" height="160" viewBox="0 0 776 160">
    <path d="M0 70 C150 10 300 110 450 60 S700 20 776 50 V160 H0Z" fill="#dbeaf8"/>
    <path d="M0 110 C180 60 330 150 500 100 S700 80 776 95 V160 H0Z" fill="#c9e0f5"/>
    <path d="M0 140 C200 110 380 170 560 130 S720 130 776 135 V160 H0Z" fill="#ffffff"/>
  </svg>
  <h1 class="hero-title">Get best<br>insurance deals</h1>
  <p class="hero-sub">Best insurance helps you to get the best insurance quotes fast and easily</p>
  <a class="btn-start" href="#">GET STARTED</a>
  <div class="hero-art" role="img" aria-label="Illustration of a family under a protective umbrella surrounded by insurance icons"></div>
  <div class="phone">
    <div class="phone-badge"></div>
    <div class="phone-title">Get a Quote</div>
    <div class="field" style="top:84px">Full Name</div>
    <div class="field" style="top:104px">Email Address</div>
    <div class="field" style="top:124px">Mobile</div>
    <div class="phone-submit"></div>
  </div>
</section>

<header class="site-header">
  <div class="brand">JISTOTAPLUS.CZ</div>
  <nav class="main-nav"><a>Home</a><a>About Us</a><a>Services</a><a>Contact</a></nav>
  <a class="btn-login" href="#">LOGIN</a>
  <a class="btn-register" href="#">REGISTER</a>
</header>

<main>
  <h2 class="section-title" style="top:360px">OUR SERVICES</h2>
  <p class="section-lead" style="top:388px">Simple and clear cover for every part of your life. Compare plans, choose what suits you and manage your policy online at any time. Our team is ready to help with claims, questions and advice whenever you need it.</p>

  <div class="slider-arrow" style="left:112px"></div>
  <div class="slider-arrow" style="left:648px"></div>

  <article class="service-card" style="left:166px">
    <div class="service-icon" role="img" aria-label="Car icon" style="background:#e94b3c"></div>
    <div class="service-name">CAR INSURANCE</div>
    <p class="service-text">Full cover for your car on every road trip</p>
  </article>
  <article class="service-card" style="left:334px">
    <div class="service-icon" role="img" aria-label="House icon" style="background:#f0a53a"></div>
    <div class="service-name">HOME INSURANCE</div>
    <p class="service-text">Protect your home and all your belongings</p>
  </article>
  <article class="service-card" style="left:502px">
    <div class="service-icon" role="img" aria-label="Boat icon" style="background:#2d5fa8"></div>
    <div class="service-name">BOAT INSURANCE</div>
    <p class="service-text">Sail with peace of mind on any water</p>
  </article>

  <svg class="abs" style="left:0;top:600px" width="776" height="120" viewBox="0 0 776 120">
    <path d="M0 40 C160 0 300 80 460 40 S700 10 776 30 V90 C620 120 460 60 300 95 S80 110 0 85Z" fill="#d5e8f8"/>
    <path d="M0 60 C180 20 320 100 480 60 S700 35 776 50 V80 C620 105 460 55 300 85 S80 95 0 75Z" fill="#c2ddf4"/>
  </svg>

  <h2 class="section-title" style="top:752px">ABOUT US</h2>
  <p class="section-lead" style="top:780px">We are a young team that makes insurance easy to understand. We compare offers from trusted partners so you always get fair prices and honest help.</p>

  <div class="about-art" role="img" aria-label="Laptop screen showing the insurance dashboard with category icons"></div>
  <h3 class="about-heading">About Insurance</h3>
  <p class="about-text">Insurance gives you support when the unexpected happens. Choose cover for your car, home or boat and get clear terms, quick claims and a team that is always on your side.</p>
  <a class="btn-more" href="#">LEARN MORE</a>
</main>

<footer class="site-footer">
  <div class="footer-brand">JISTOTAPLUS.CZ</div>
  <p class="footer-about">We are a young and friendly insurance team making cover simple, fair and fast for everyone.</p>
  <span class="social" style="left:28px;background:#3b5998"></span>
  <span class="social" style="left:44px;background:#1da1f2"></span>
  <span class="social" style="left:60px;background:#dd4b39"></span>
  <span class="social" style="left:76px;background:#cb2027"></span>

  <div class="footer-col" style="left:284px">
    <h4>Quick Link</h4>
    Home<br>About Us<br>Services<br>My Policy<br>Join Our Team
  </div>
  <div class="footer-col" style="left:384px">
    <h4>Need Help?</h4>
    FAQ<br>Claims<br>Privacy Policy<br>Terms and Conditions
  </div>
  <div class="footer-col" style="left:500px">
    <h4>CONTACT US</h4>
    <div class="contact-row"><svg width="6" height="6" viewBox="0 0 10 10"><path d="M2 1l2 2-1 1.5c.8 1.5 1.8 2.5 3 3L7.5 6l2 2-1.5 1.5C4 9 1 6 .5 1.5Z" fill="#1f6fe5"/></svg>Phone &nbsp;+420 601 482 317</div>
    <div class="contact-row"><svg width="6" height="6" viewBox="0 0 10 10"><rect x="0.5" y="2" width="9" height="6" fill="none" stroke="#1f6fe5"/><path d="M.5 2l4.5 3.5L9.5 2" fill="none" stroke="#1f6fe5"/></svg>Email &nbsp;info@jistotaplus.cz</div>
  </div>
  <div class="subscribe">Email<span class="subscribe-btn"></span></div>
  <p class="copyright">Copyright © 2017 JistotaPlus.cz All rights reserved</p>
</footer>

</body>
</html>
```